Online Psychiatry business - Business Card

I need a business card design. The target audience is busy professionals of any field (this therapy appeals best to 24-35 year olds). It involves psychiatry by tele-medicine (or video-conference). Nothing on it should be a giveaway that it's about mental health. Professional design with silver or gold as the primary colors appeals to me. The card must be as simple and as uncluttered as possible. Some color and flowing design on the edge of the card appeals to me.
CrestLumaCareNet.com should probably appear in the center of the card and stand out, i.e. bold lettering, and easy to read, no cursive, but Ariel Black. Some where below this, should appear "Too Busy to Take Care of Yourself? Think again." Since this isn't office based, I don't think an office address is necessary and limits clutter.
Information that does need to appear is my name: Gerald Mewkinson, MD
General phone number: 618-472-9086. I'm hoping to get an 24-hour answering service soon so leave a little room for this. In addition I want to include two email addresses:
CrestLumaCareNet@mailvora.com and CrestLumaCare247@mailvora.com
Updates

I like the designs. I would like someone to put the website in bold in the center

 as most have been doing with a smaller font reminder nearby saying "No time" etc.
but I'd like to put my name down in the corner with the rest of the contact material.
Black print against a white or grey background appeals to me, with darker silver artwork near the sides (simple abstract, like wavy lines or something you can one up with that works. 
thanks

I ve tried to provide as much feedback as possible given my time limits, so if you have extra questions, please feel free to email. I tried to attach a file of a business card I really like but make be difficult to actually manufacture. I'm going to send you a link to the photo. The card has a pull tab. There is not much information on the outside. In fact, if you were to design the outside, I would just print : Too Busy to Take Care of Yourself? Think Again.

When you pull the tab the remaining information is on the bottom half of the card. Please don't use the color pink!!!!
http://www.printfolkgallery.net/2009/05/100-really-creative-business-cards/
It is the 39th photo on the list, about 2/3ds of the way down the page. It is titled: Ruvelinkiste

#7 and #16 have an appeal to me, except for the dot patterns
Hope this helps

I'm running out of time and energy. I 've been trying to give do down the list and give  individual feedback but I won't be able to do that anymore.

So if you have any specific questions, write me, and again thank you for all your effort!!

I know i received your files, including your zip files, Tolkra,

but Milos, did you send me the files including ZIP on project 5139624?
thanks

Target Market(s)

Working professionals and executive, attorneys, etc.

Industry/Entity Type

Business

Logo Text

Don't Have Time to Take Care of Yourself? Think Again.

Logo styles of interest
Pictorial/Combination Logo
Wordmark Logo
Font styles to use
Other font styles liked:
• Ariel Black appeals to me the most

Requirements
Must have
• Want to emphasize that the website must be obvious, easily found (The CrestLumaCareNet.com)
For that reason i'd like the card to be white, and minimal decoration on one or both sides just to add some style and color
Nice to have
• A Very uncluttered, elegant design, and something that makes it stick in your head-doesn't everyone want the last?
Should not have
• Nothing on the card that give it away that this is about psychiatry, such as brain or other symbol, but also nothing that gives it away as a medical business, such as a stethoscope or red cross or anything.

```html
<!DOCTYPE html>
<html lang="en">
<head>
<meta charset="utf-8">
<title>CrestLumaCareNet.com – Business Card</title>
<link href="https://fonts.googleapis.com/css2?family=Archivo+Black&family=Open+Sans:wght@400;600;700&family=Tinos&display=swap" rel="stylesheet">
<style>
  :root {
    --backdrop: #e9e6e1;
    --card-white: #ffffff;
    --card-mist: #ececec;
    --ink: #3a3a3a;
    --ink-dark: #1f1f1f;
    --accent-orange: #e8951f;
    --wave-light: #fff4a6;
    --wave-deep: #f1a02c;
    --swoosh-grey: #6f6f6f;
    --swoosh-soft: #9a9a9a;
    --gold-light: #fbf1a8;
    --gold-mid: #e6cf78;
    --gold-deep: #b98d3a;
    --gold-note: #fff7dc;
  }
  * { box-sizing: border-box; margin: 0; padding: 0; }
  html, body {
    width: 1200px; height: 418px; overflow: hidden;
    background: var(--backdrop);
  }
  .sheet { position: relative; width: 1200px; height: 418px; }
  .card {
    position: absolute; top: 77px; width: 468px; height: 266px;
    overflow: hidden;
    box-shadow: 0 3px 10px rgba(0,0,0,0.25);
  }
  .card--front {
    left: 118px;
    background: radial-gradient(ellipse at 50% 35%, var(--card-white) 55%, var(--card-mist) 100%);
  }
  .card--back {
    left: 614px;
    background: linear-gradient(180deg, var(--gold-light) 0%, var(--gold-mid) 55%, var(--gold-deep) 100%);
  }
  .card__art { position: absolute; inset: 0; }

  .site-name {
    position: absolute; left: 0; right: 0;
    text-align: center;
    font-family: "Archivo Black", "Arial Black", sans-serif;
    font-size: 25px; letter-spacing: 0.2px;
  }
  .card--front .site-name { top: 82px; color: var(--ink); }
  .card--back .site-name {
    top: 94px; color: #fff;
    text-shadow: 1px 2px 3px rgba(0,0,0,0.45);
  }

  .tagline {
    position: absolute; left: 18px; bottom: 22px;
    font-family: "Open Sans", sans-serif; font-weight: 700;
    font-size: 11.5px; line-height: 1.3; color: var(--ink-dark);
  }

  .contact {
    position: absolute; right: 18px; top: 168px;
    text-align: right;
    font-family: "Open Sans", sans-serif; color: var(--ink-dark);
  }
  .contact__name { font-size: 12px; font-weight: 700; margin-bottom: 4px; }
  .contact__phone { font-size: 13px; margin-bottom: 10px; }
  .contact__label { color: var(--accent-orange); }
  .contact__email { font-size: 10px; line-height: 1.5; }

  .slogan {
    position: absolute; left: 0; right: 0; top: 134px;
    text-align: center;
    font-family: "Open Sans", sans-serif; font-weight: 700;
    font-size: 11px; letter-spacing: 0.6px; color: var(--ink-dark);
  }
  .service-note {
    position: absolute; left: 0; right: 0; top: 237px;
    text-align: center;
    font-family: "Tinos", serif; font-size: 10px; color: var(--gold-note);
  }
</style>
</head>
<body>
<main class="sheet">

  <section class="card card--front">
    <svg class="card__art" viewBox="0 0 468 266" aria-hidden="true">
      <defs>
        <linearGradient id="wave-fill" x1="0" y1="0" x2="1" y2="1">
          <stop offset="0" stop-color="var(--wave-light)"/>
          <stop offset="1" stop-color="var(--wave-deep)"/>
        </linearGradient>
      </defs>
      <path d="M0,186 C90,180 190,200 252,266 L0,266 Z" fill="url(#wave-fill)"/>
      <path d="M0,180 C100,172 205,196 264,266" fill="none" stroke="var(--swoosh-grey)" stroke-width="5"/>
      <path d="M20,170 C125,162 222,188 276,266" fill="none" stroke="var(--swoosh-soft)" stroke-width="1.5"/>
    </svg>
    <h1 class="site-name">CrestLumaCareNet.com</h1>
    <p class="tagline">Too Busy to Take Care of<br>Yourself?&nbsp; Think again.</p>
    <div class="contact">
      <p class="contact__name">Gerald Mewkinson, MD</p>
      <p class="contact__phone"><span class="contact__label">General Phone:</span> 618-472-9086</p>
      <p class="contact__email">CrestLumaCareNet@mailvora.com</p>
      <p class="contact__email">CrestLumaCare247@mailvora.com</p>
    </div>
  </section>

  <section class="card card--back">
    <svg class="card__art" viewBox="0 0 468 266" aria-hidden="true">
      <path d="M340,0 C390,12 430,22 468,34 L468,0 Z" fill="#fffbe0" opacity="0.85"/>
      <path d="M336,0 C386,14 428,26 468,38" fill="none" stroke="var(--swoosh-grey)" stroke-width="3"/>
    </svg>
    <h2 class="site-name">CrestLumaCareNet.com</h2>
    <p class="slogan">NOT ENOUGH TIME TO CARE FOR YOURSELF</p>
    <p class="service-note">24-hour answering service</p>
  </section>

</main>
</body>
</html>
```